Create a Microsoft word or excel document

Please create a Microsoft office template I can use to update panel schedules, please choose excel or word.

The first attachment is a good example I found on Plimbex, I would like this exact template but I would like to change the writing at the top of the page, the second attachment is what I want the top of the template to be, the bulk of the page can remain. Please only go to #45-46. Please make this easy so I can simply type in the panel directory without having to delete lines and mess up the template that you are creating.

Edit; Please make the Volts, phases and wire section blank.

Thanks,

```html
<!DOCTYPE html>
<html lang="en">
<head>
<meta charset="utf-8">
<title>Branch Panel Schedule</title>
<link href="https://fonts.googleapis.com/css2?family=Carlito:wght@400;700&family=Caladea:wght@700&display=swap" rel="stylesheet">
<style>
  :root {
    --paper: #ffffff;
    --ink: #000000;
    --label-ink: #333333;
    --grid: #8c8c8c;
    --grid-soft: #c8c8c8;
    --frame: #1a1a1a;
    --phase-shade: #dedede;
    --header-fill: #f2f2f2;
  }
  html, body {
    margin: 0;
    padding: 0;
    width: 1200px;
    height: 485px;
    overflow: hidden;
    background: var(--paper);
  }
  .schedule {
    position: relative;
    width: 1200px;
    height: 485px;
    font-family: "Carlito", "Calibri", sans-serif;
    color: var(--ink);
    border-left: 1px solid var(--grid-soft);
    box-sizing: border-box;
  }
  .panel-title {
    position: absolute;
    left: 239px;
    top: 6px;
    font-family: "Caladea", "Cambria", serif;
    font-weight: 700;
    font-size: 12px;
  }
  .field {
    position: absolute;
    display: flex;
    align-items: flex-end;
    font-size: 10.5px;
    color: var(--label-ink);
  }
  .field-label {
    text-align: right;
    padding-right: 4px;
  }
  .field-line {
    border-bottom: 1px solid var(--ink);
    height: 12px;
  }
  .field--title { left: 314px; top: 8px; }
  .field--title .field-line { width: 286px; }
  .field--main .field-label { width: 86px; }
  .field--main .field-line { width: 286px; }
  .field--main { left: 228px; }
  .field--elec .field-label { width: 90px; }
  .field--elec .field-line { width: 115px; }
  .field--elec { left: 623px; }
  .row-1 { top: 46px; }
  .row-2 { top: 68px; }
  .row-3 { top: 89px; }

  .circuit-table {
    position: absolute;
    left: 0;
    top: 131px;
    width: 1200px;
    border-collapse: collapse;
    table-layout: fixed;
    border: 2px solid var(--frame);
    font-size: 10px;
  }
  .circuit-table th {
    height: 16px;
    font-weight: 700;
    font-size: 11px;
    background: var(--header-fill);
    border: 1px solid var(--grid);
    border-bottom: 2px solid var(--frame);
    padding: 0;
  }
  .circuit-table td {
    height: 13.5px;
    padding: 0;
    border: 1px solid var(--grid);
    text-align: center;
    line-height: 12px;
  }
  .circuit-table .phase-cell { border-color: var(--grid-soft); }
  .circuit-table .phase-cell.is-shaded { background: var(--phase-shade); }
  .circuit-table .phase-start { border-left: 1px solid var(--frame); }
  .circuit-table .phase-end { border-right: 1px solid var(--frame); }
</style>
</head>
<body>
<main class="schedule">
  <div class="panel-title">Branch Panel:</div>
  <div class="field field--title"><span class="field-line"></span></div>

  <div class="field field--main row-1"><span class="field-label">Location:</span><span class="field-line"></span></div>
  <div class="field field--main row-2"><span class="field-label">Supply from:</span><span class="field-line"></span></div>
  <div class="field field--main row-3"><span class="field-label">Enclosure:</span><span class="field-line"></span></div>

  <div class="field field--elec row-1"><span class="field-label">Volts:</span><span class="field-line"></span></div>
  <div class="field field--elec row-2"><span class="field-label">Phases:</span><span class="field-line"></span></div>
  <div class="field field--elec row-3"><span class="field-label">Wires:</span><span class="field-line"></span></div>

  <table class="circuit-table">
    <colgroup>
      <col style="width:35px"><col style="width:279px"><col style="width:55px"><col style="width:54px">
      <col style="width:60px"><col style="width:59px"><col style="width:59px"><col style="width:59px"><col style="width:59px"><col style="width:59px">
      <col style="width:54px"><col style="width:55px"><col style="width:280px"><col style="width:33px">
    </colgroup>
    <thead>
      <tr>
        <th>CKT</th><th>Circuit Description</th><th>Trip</th><th>Poles</th>
        <th colspan="2" class="phase-start phase-end">A</th>
        <th colspan="2" class="phase-start phase-end">B</th>
        <th colspan="2" class="phase-start phase-end">C</th>
        <th>Poles</th><th>Trip</th><th>Circuit Description</th><th>CKT</th>
      </tr>
    </thead>
    <tbody>
      <tr><td>1</td><td></td><td></td><td></td><td class="phase-cell phase-start"></td><td class="phase-cell phase-end"></td><td class="phase-cell phase-start is-shaded"></td><td class="phase-cell phase-end is-shaded"></td><td class="phase-cell phase-start is-shaded"></td><td class="phase-cell phase-end is-shaded"></td><td></td><td></td><td></td><td>2</td></tr>
      <tr><td>3</td><td></td><td></td><td></td><td class="phase-cell phase-start is-shaded"></td><td class="phase-cell phase-end is-shaded"></td><td class="phase-cell phase-start"></td><td class="phase-cell phase-end"></td><td class="phase-cell phase-start is-shaded"></td><td class="phase-cell phase-end is-shaded"></td><td></td><td></td><td></td><td>4</td></tr>
      <tr><td>5</td><td></td><td></td><td></td><td class="phase-cell phase-start is-shaded"></td><td class="phase-cell phase-end is-shaded"></td><td class="phase-cell phase-start is-shaded"></td><td class="phase-cell phase-end is-shaded"></td><td class="phase-cell phase-start"></td><td class="phase-cell phase-end"></td><td></td><td></td><td></td><td>6</td></tr>
      <tr><td>7</td><td></td><td></td><td></td><td class="phase-cell phase-start"></td><td class="phase-cell phase-end"></td><td class="phase-cell phase-start is-shaded"></td><td class="phase-cell phase-end is-shaded"></td><td class="phase-cell phase-start is-shaded"></td><td class="phase-cell phase-end is-shaded"></td><td></td><td></td><td></td><td>8</td></tr>
      <tr><td>9</td><td></td><td></td><td></td><td class="phase-cell phase-start is-shaded"></td><td class="phase-cell phase-end is-shaded"></td><td class="phase-cell phase-start"></td><td class="phase-cell phase-end"></td><td class="phase-cell phase-start is-shaded"></td><td class="phase-cell phase-end is-shaded"></td><td></td><td></td><td></td><td>10</td></tr>
      <tr><td>11</td><td></td><td></td><td></td><td class="phase-cell phase-start is-shaded"></td><td class="phase-cell phase-end is-shaded"></td><td class="phase-cell phase-start is-shaded"></td><td class="phase-cell phase-end is-shaded"></td><td class="phase-cell phase-start"></td><td class="phase-cell phase-end"></td><td></td><td></td><td></td><td>12</td></tr>
      <tr><td>13</td><td></td><td></td><td></td><td class="phase-cell phase-start"></td><td class="phase-cell phase-end"></td><td class="phase-cell phase-start is-shaded"></td><td class="phase-cell phase-end is-shaded"></td><td class="phase-cell phase-start is-shaded"></td><td class="phase-cell phase-end is-shaded"></td><td></td><td></td><td></td><td>14</td></tr>
      <tr><td>15</td><td></td><td></td><td></td><td class="phase-cell phase-start is-shaded"></td><td class="phase-cell phase-end is-shaded"></td><td class="phase-cell phase-start"></td><td class="phase-cell phase-end"></td><td class="phase-cell phase-start is-shaded"></td><td class="phase-cell phase-end is-shaded"></td><td></td><td></td><td></td><td>16</td></tr>
      <tr><td>17</td><td></td><td></td><td></td><td class="phase-cell phase-start is-shaded"></td><td class="phase-cell phase-end is-shaded"></td><td class="phase-cell phase-start is-shaded"></td><td class="phase-cell phase-end is-shaded"></td><td class="phase-cell phase-start"></td><td class="phase-cell phase-end"></td><td></td><td></td><td></td><td>18</td></tr>
      <tr><td>19</td><td></td><td></td><td></td><td class="phase-cell phase-start"></td><td class="phase-cell phase-end"></td><td class="phase-cell phase-start is-shaded"></td><td class="phase-cell phase-end is-shaded"></td><td class="phase-cell phase-start is-shaded"></td><td class="phase-cell phase-end is-shaded"></td><td></td><td></td><td></td><td>20</td></tr>
      <tr><td>21</td><td></td><td></td><td></td><td class="phase-cell phase-start is-shaded"></td><td class="phase-cell phase-end is-shaded"></td><td class="phase-cell phase-start"></td><td class="phase-cell phase-end"></td><td class="phase-cell phase-start is-shaded"></td><td class="phase-cell phase-end is-shaded"></td><td></td><td></td><td></td><td>22</td></tr>
      <tr><td>23</td><td></td><td></td><td></td><td class="phase-cell phase-start is-shaded"></td><td class="phase-cell phase-end is-shaded"></td><td class="phase-cell phase-start is-shaded"></td><td class="phase-cell phase-end is-shaded"></td><td class="phase-cell phase-start"></td><td class="phase-cell phase-end"></td><td></td><td></td><td></td><td>24</td></tr>
      <tr><td>25</td><td></td><td></td><td></td><td class="phase-cell phase-start"></td><td class="phase-cell phase-end"></td><td class="phase-cell phase-start is-shaded"></td><td class="phase-cell phase-end is-shaded"></td><td class="phase-cell phase-start is-shaded"></td><td class="phase-cell phase-end is-shaded"></td><td></td><td></td><td></td><td>26</td></tr>
      <tr><td>27</td><td></td><td></td><td></td><td class="phase-cell phase-start is-shaded"></td><td class="phase-cell phase-end is-shaded"></td><td class="phase-cell phase-start"></td><td class="phase-cell phase-end"></td><td class="phase-cell phase-start is-shaded"></td><td class="phase-cell phase-end is-shaded"></td><td></td><td></td><td></td><td>28</td></tr>
      <tr><td>29</td><td></td><td></td><td></td><td class="phase-cell phase-start is-shaded"></td><td class="phase-cell phase-end is-shaded"></td><td class="phase-cell phase-start is-shaded"></td><td class="phase-cell phase-end is-shaded"></td><td class="phase-cell phase-start"></td><td class="phase-cell phase-end"></td><td></td><td></td><td></td><td>30</td></tr>
      <tr><td>31</td><td></td><td></td><td></td><td class="phase-cell phase-start"></td><td class="phase-cell phase-end"></td><td class="phase-cell phase-start is-shaded"></td><td class="phase-cell phase-end is-shaded"></td><td class="phase-cell phase-start is-shaded"></td><td class="phase-cell phase-end is-shaded"></td><td></td><td></td><td></td><td>32</td></tr>
      <tr><td>33</td><td></td><td></td><td></td><td class="phase-cell phase-start is-shaded"></td><td class="phase-cell phase-end is-shaded"></td><td class="phase-cell phase-start"></td><td class="phase-cell phase-end"></td><td class="phase-cell phase-start is-shaded"></td><td class="phase-cell phase-end is-shaded"></td><td></td><td></td><td></td><td>34</td></tr>
      <tr><td>35</td><td></td><td></td><td></td><td class="phase-cell phase-start is-shaded"></td><td class="phase-cell phase-end is-shaded"></td><td class="phase-cell phase-start is-shaded"></td><td class="phase-cell phase-end is-shaded"></td><td class="phase-cell phase-start"></td><td class="phase-cell phase-end"></td><td></td><td></td><td></td><td>36</td></tr>
      <tr><td>37</td><td></td><td></td><td></td><td class="phase-cell phase-start"></td><td class="phase-cell phase-end"></td><td class="phase-cell phase-start is-shaded"></td><td class="phase-cell phase-end is-shaded"></td><td class="phase-cell phase-start is-shaded"></td><td class="phase-cell phase-end is-shaded"></td><td></td><td></td><td></td><td>38</td></tr>
      <tr><td>39</td><td></td><td></td><td></td><td class="phase-cell phase-start is-shaded"></td><td class="phase-cell phase-end is-shaded"></td><td class="phase-cell phase-start"></td><td class="phase-cell phase-end"></td><td class="phase-cell phase-start is-shaded"></td><td class="phase-cell phase-end is-shaded"></td><td></td><td></td><td></td><td>40</td></tr>
      <tr><td>41</td><td></td><td></td><td></td><td class="phase-cell phase-start is-shaded"></td><td class="phase-cell phase-end is-shaded"></td><td class="phase-cell phase-start is-shaded"></td><td class="phase-cell phase-end is-shaded"></td><td class="phase-cell phase-start"></td><td class="phase-cell phase-end"></td><td></td><td></td><td></td><td>42</td></tr>
      <tr><td>43</td><td></td><td></td><td></td><td class="phase-cell phase-start"></td><td class="phase-cell phase-end"></td><td class="phase-cell phase-start is-shaded"></td><td class="phase-cell phase-end is-shaded"></td><td class="phase-cell phase-start is-shaded"></td><td class="phase-cell phase-end is-shaded"></td><td></td><td></td><td></td><td>44</td></tr>
      <tr><td>45</td><td></td><td></td><td></td><td class="phase-cell phase-start is-shaded"></td><td class="phase-cell phase-end is-shaded"></td><td class="phase-cell phase-start"></td><td class="phase-cell phase-end"></td><td class="phase-cell phase-start is-shaded"></td><td class="phase-cell phase-end is-shaded"></td><td></td><td></td><td></td><td>46</td></tr>
    </tbody>
  </table>
</main>
</body>
</html>
```